Quote Cards for Social Media KL

I would like to put these quotes over one of the pictures attached; One Quote per picture, and I want the quote to be bold or easy to read as well. I provided a few reference graphics that I really like as examples below. In very small letters at the bottom add @KLVarneyDaily

All of the pictures are attached; you can pick any photo and add one quote to it; but no stock photography

Target Market(s)

women trying to lose weight

Requirements
Must have
• quotes and pictures attached
Should not have
• no stock photography

```html
<!DOCTYPE html>
<html lang="en">
<head>
<meta charset="utf-8">
<title>Quote Card – Flatter Belly</title>
<link rel="stylesheet" href="https://fonts.googleapis.com/css2?family=Bebas+Neue&family=Montserrat:wght@500&display=swap">
<style>
  :root {
    --panel-light: #de4ca0;
    --panel-mid: #c4307f;
    --panel-dark: #9c1c68;
    --photo-light: #e6ddd2;
    --photo-mid: #c9a27c;
    --photo-dark: #2a2324;
    --quote-white: #ffffff;
    --quote-shadow: #2b0a1c;
  }
  html, body {
    margin: 0;
    padding: 0;
    width: 1200px;
    height: 1200px;
    overflow: hidden;
    background: #ffffff;
  }
  .quote-card {
    position: relative;
    width: 1200px;
    height: 1200px;
    overflow: hidden;
  }
  .portrait-area {
    position: absolute;
    left: 0;
    top: 0;
    width: 606px;
    height: 1200px;
    background: linear-gradient(160deg, var(--photo-light) 0%, var(--photo-light) 30%, var(--photo-mid) 55%, var(--photo-mid) 80%, var(--photo-dark) 100%);
  }
  .quote-panel {
    position: absolute;
    left: 606px;
    top: 0;
    width: 594px;
    height: 1200px;
    background: radial-gradient(ellipse 75% 60% at 50% 50%, var(--panel-light) 0%, var(--panel-mid) 55%, var(--panel-dark) 100%);
  }
  .quote-text {
    position: absolute;
    left: 0;
    right: 0;
    top: 284px;
    margin: 0;
    text-align: center;
    font-family: "Bebas Neue", "Oswald", sans-serif;
    font-weight: 400;
    font-size: 87px;
    line-height: 94px;
    letter-spacing: 1px;
    color: var(--quote-white);
    text-shadow: 3px 4px 0 var(--quote-shadow);
  }
  .handle {
    position: absolute;
    left: 0;
    right: 0;
    top: 1088px;
    margin: 0;
    text-align: center;
    font-family: "Montserrat", sans-serif;
    font-weight: 500;
    font-size: 28px;
    letter-spacing: 0.5px;
    color: var(--quote-white);
  }
</style>
</head>
<body>
  <main class="quote-card">
    <div class="portrait-area" role="img" aria-label="Photo of a smiling woman with wavy brown hair in a tan ribbed turtleneck, long silver pendant necklace and black high-waisted trousers, hand on hip, against a light stone wall"></div>
    <section class="quote-panel">
      <p class="quote-text">Wake up<br>tomorrow<br>with a flatter<br>belly- yes,<br>this overnight<br>remedy works<br>like magic!</p>
      <p class="handle">@KLVarneyDaily</p>
    </section>
  </main>
</body>
</html>
```